Renewable energy company needs modern memorable marketing brochure

We have an 8 page marketing brochure which was created in house. This needs to be revamped and modernised to stand out from our competitors in Australia, Chile and the UK. The brochure should depict us as a professional and dynamic company and instil confidence in prospective clients that we do a professional job. Once the design is finalised we will need a country specific document in the correct language i.e. Spanish for Chile. We are happy to pay for these iterations. We have a company logo which we would like incorporated into the brochure and the colours from the logo utilised where appropriate in the overall design. I have uploaded our existing brochure for an example of the content that the brochure needs to have and can upload the images separately if they are needed. Images in the brochure need to be copyright free and we have lots of photos in-house. I have added all the images from the last brochure and also the text in Indesign so it can be copied easily if needed.

Target Market(s)

landowners and companies

Industry/Entity Type

It Company

Requirements
Must have
• A clean modern look with some colours taken from the logo colour. Be easy to print in various countries.

```html
<!DOCTYPE html>
<html lang="en">
<head>
<meta charset="utf-8">
<title>Radiant Fields – Brochure Cover Spread</title>
<link href="https://fonts.googleapis.com/css2?family=Barlow:wght@400;500&family=Arimo:wght@400;700&display=swap" rel="stylesheet">
<style>
  :root {
    --backdrop: #e8e6e3;
    --paper: #ffffff;
    --ink: #1e1e1e;
    --ink-soft: #2b2b2b;
    --rule: #1f1f1f;
    --brand-grey: #5a5a5a;
    --brand-light: #b9b9b9;
    --field-green: #5f9a3a;
    --field-light: #a7c77a;
    --panel-blue: #1d2756;
    --sky: #c9d3dc;
  }
  * { box-sizing: border-box; margin: 0; padding: 0; }
  html, body { width: 1200px; height: 1200px; overflow: hidden; background: var(--backdrop); }
  .spread {
    position: absolute; left: 0; top: 176px;
    width: 1200px; height: 848px;
    background: var(--paper);
    box-shadow: 0 2px 6px rgba(0,0,0,.18);
    font-family: "Arimo", Arial, sans-serif;
    color: var(--ink);
  }
  .photo { position: absolute; }
  .photo-underframe {
    left: 0; top: 0; width: 600px; height: 255px;
    background: linear-gradient(180deg, #8f9498 0%, #c9ccc8 30%, #88b45a 62%, var(--field-green) 100%);
  }
  .rule-left { position: absolute; left: 0; top: 255px; width: 600px; height: 5px; background: var(--rule); }
  .rule-right { position: absolute; left: 600px; top: 250px; width: 600px; height: 5px; background: var(--rule); }
  .photo-aerial {
    left: 600px; top: 255px; width: 600px; height: 283px;
    background: linear-gradient(180deg, var(--sky) 0%, #b9b79a 10%, #6f8a4a 28%, #2b3566 55%, var(--panel-blue) 100%);
  }
  .photo-round { border-radius: 50%; border: 0; }
  .photo-tree {
    left: 815px; top: 458px; width: 202px; height: 204px;
    background: radial-gradient(circle at 45% 30%, #8fb44c 0%, #5a7f31 45%, #7f8f86 75%, #4d5a52 100%);
  }
  .photo-panel {
    left: 1015px; top: 484px; width: 140px; height: 142px;
    background: linear-gradient(200deg, #dfe6ec 0%, #9fb1c4 40%, #3f5f86 75%, #2a3d5c 100%);
  }
  .brand {
    position: absolute; left: 905px; top: 76px;
    display: flex; align-items: center; gap: 24px;
  }
  .brand-mark { width: 86px; height: 86px; border-radius: 50%; background: var(--brand-light); }
  .brand-name {
    font-family: "Barlow", sans-serif; font-weight: 400;
    font-size: 31px; line-height: 30px; letter-spacing: 1.5px;
    color: var(--brand-grey);
  }
  .contact { position: absolute; left: 19px; top: 515px; width: 440px; font-size: 11.5px; line-height: 15px; color: var(--ink-soft); }
  .contact h2 { font-size: 11.5px; font-weight: 700; text-transform: uppercase; }
  .contact .intro { margin-bottom: 30px; }
  .contact h3 { font-size: 14px; font-weight: 400; line-height: 16px; }
  .contact .person { margin-bottom: 14px; }
  .contact .name { font-weight: 700; }
  .headline { position: absolute; left: 618px; top: 738px; font-family: "Barlow", sans-serif; color: var(--ink); }
  .headline h1 { font-size: 38px; font-weight: 500; line-height: 40px; }
  .headline p { font-size: 21px; font-weight: 400; line-height: 25px; text-transform: uppercase; }
</style>
</head>
<body>
  <main class="spread">
    <div class="photo photo-underframe" role="img" aria-label="Ground-level view beneath rows of raised solar panels over tall green grass"></div>
    <div class="rule-left"></div>

    <div class="brand">
      <span class="brand-mark"></span>
      <span class="brand-name">RADIANT<br>FIELDS</span>
    </div>

    <div class="rule-right"></div>
    <div class="photo photo-aerial" role="img" aria-label="Aerial view of a large solar farm among green countryside fields"></div>
    <div class="photo photo-round photo-tree" role="img" aria-label="Solar panels reflecting a leafy tree"></div>
    <div class="photo photo-round photo-panel" role="img" aria-label="Close-up of a solar panel reflecting blue sky"></div>

    <section class="contact">
      <h2>Contact Details</h2>
      <p class="intro">If you are interested to learn more about securing a long term income stream<br>from a Radiant Fields solar farm on your land please contact us</p>
      <h3>Australia</h3>
      <div class="person">
        <p class="name">Liam Harrow</p>
        <p>Business Development Associate</p>
        <p>liam.harrow@radiantfields.com.au</p>
        <p>+61 (0) 400 123 456</p>
      </div>
      <div class="person">
        <p class="name">Owen Merrick</p>
        <p>Business Development Associate</p>
        <p>owen.merrick@radiantfields.com.au</p>
        <p>+61 (0) 400 654 321</p>
      </div>
      <div class="person">
        <p class="name">Radiant Fields PTY. Ltd.</p>
        <p>c/o Bellwood Partners, Level 2,<br>48 Harbour Rd, Eastbrook,<br>Qld, 4010 Australia</p>
        <p>www.radiantfields.com.au</p>
      </div>
    </section>

    <section class="headline">
      <h1>INFINITE ENERGY</h1>
      <p>Use your land to harvest<br>energy from the sun</p>
    </section>
  </main>
</body>
</html>
```